Wardoona Contracting Pty Ltd.

We need a corporate brand/logo for a new company. The company is represented by Indigenous Australians in Western Australias far north West. The aea is the Kimberley. The work we are involved in is contracting our services to companies. Our services range from heavy earth working machinary to landscape rehabilitation including revegetation. Other services we provide are demolition, contaminated sites and water management. We are essentially a services provider for hire. We tender mostly for contracts wit hmining companies.

```html
<!DOCTYPE html>
<html lang="en">
<head>
<meta charset="utf-8">
<title>Wardoona Contracting – Business Cards</title>
<link rel="stylesheet" href="https://fonts.googleapis.com/css2?family=Archivo:wght@500;600&family=Montserrat:wght@800&family=Open+Sans:wght@600&display=swap">
<style>
  :root {
    --ink: #111417;
    --navy: #15323d;
    --orange: #f0713a;
    --amber: #f9ad3c;
    --red: #c8202f;
    --frame: #f6b25a;
    --paper: #ffffff;
  }
  * { box-sizing: border-box; margin: 0; padding: 0; }
  html, body { width: 1200px; height: 864px; overflow: hidden; background: var(--paper); }
  .sheet { position: relative; width: 1200px; height: 864px; }

  .card {
    position: absolute;
    background: var(--paper);
    border: 1px solid var(--frame);
    overflow: hidden;
  }

  /* Front card */
  .card--front { left: 317px; top: 0; width: 564px; height: 359px; }
  .brand-mark {
    position: absolute; left: 50%; top: 78px;
    width: 90px; height: 90px; margin-left: -45px;
    border-radius: 50%; background: var(--orange);
  }
  .brand-name {
    position: absolute; left: 0; right: 0; top: 226px;
    text-align: center;
    font-family: "Montserrat", sans-serif; font-weight: 800;
    font-size: 29px; letter-spacing: 1.2px; color: var(--navy);
  }
  .front-band {
    position: absolute; left: 0; right: 0; bottom: 0; height: 60px;
    background: var(--orange);
  }
  .front-band__web {
    display: block; text-align: center; padding-top: 7px;
    font-family: "Open Sans", sans-serif; font-weight: 600;
    font-size: 12.5px; color: var(--paper);
  }

  /* Back cards */
  .card--back { top: 506px; width: 563px; height: 357px; }
  .card--darren { left: 0; }
  .card--luke { left: 636px; }

  .pattern-area {
    position: absolute; left: 0;
    background: linear-gradient(160deg, var(--amber) 0%, var(--orange) 55%, #e0603a 100%);
    border-radius: 0 50% 50% 0 / 0 50% 50% 0;
  }
  .card--darren .pattern-area { top: 44px; width: 160px; height: 268px; }
  .card--luke .pattern-area { top: 32px; width: 178px; height: 274px; }

  .person { position: absolute; left: 223px; top: 53px; width: 290px; }
  .person__name {
    font-family: "Archivo", sans-serif; font-weight: 600;
    font-size: 30px; line-height: 1; color: var(--ink);
    padding-bottom: 6px; border-bottom: 1.5px solid var(--ink);
  }
  .person__role {
    font-family: "Archivo", sans-serif; font-weight: 600;
    font-size: 22px; line-height: 1.2; color: var(--ink); margin-top: 3px;
  }

  .contacts { position: absolute; left: 223px; top: 193px; list-style: none; }
  .contacts li {
    display: flex; align-items: center; height: 29px;
    font-family: "Archivo", sans-serif; font-weight: 600;
    font-size: 15.5px; color: var(--ink);
  }
  .contacts svg { width: 22px; height: 22px; margin-right: 13px; flex: none; }
  .contacts .phone-number { font-size: 18px; letter-spacing: 0.3px; }
</style>
</head>
<body>
<main class="sheet">

  <section class="card card--front">
    <div class="brand-mark" aria-hidden="true"></div>
    <h1 class="brand-name">WARDOONA CONTRACTING</h1>
    <div class="front-band">
      <span class="front-band__web">www.wardoonacontracting.com.au</span>
    </div>
  </section>

  <section class="card card--back card--darren">
    <div class="pattern-area" role="img" aria-label="Decorative dot-painting artwork in orange, amber, red and navy"></div>
    <div class="person">
      <h2 class="person__name">Darren Whitby</h2>
      <p class="person__role">Director</p>
    </div>
    <ul class="contacts">
      <li><svg viewBox="0 0 24 24"><path d="M7 2c-2 1-3 3-2.5 6 .8 5 4.5 11 9 13.5 1.5.8 3 .5 4-.5l-3.5-4-2 1c-2-1.5-4-5-4.5-7.5l2-1L8 2z" fill="var(--ink)"/></svg><span class="phone-number">+61 400 555 128</span></li>
      <li><svg viewBox="0 0 24 24"><path d="M2 10l10-7 10 7v10H2z" fill="var(--ink)"/><path d="M2 11l10 6 10-6" stroke="#fff" stroke-width="1.5" fill="none"/></svg>darren@wardoonacontracting.com.au</li>
      <li><svg viewBox="0 0 24 24" fill="none" stroke="var(--ink)" stroke-width="1.4"><circle cx="11" cy="11" r="9"/><ellipse cx="11" cy="11" rx="4" ry="9"/><path d="M2 11h18M4 6h14M4 16h14"/><path d="M15 15l6 6" stroke-width="2.5"/></svg>www.wardoonacontracting.com.au</li>
    </ul>
  </section>

  <section class="card card--back card--luke">
    <div class="pattern-area" role="img" aria-label="Decorative dot-painting artwork in orange, amber, red and navy"></div>
    <div class="person">
      <h2 class="person__name">Luke Brennan</h2>
      <p class="person__role">Director</p>
    </div>
    <ul class="contacts">
      <li><svg viewBox="0 0 24 24"><path d="M7 2c-2 1-3 3-2.5 6 .8 5 4.5 11 9 13.5 1.5.8 3 .5 4-.5l-3.5-4-2 1c-2-1.5-4-5-4.5-7.5l2-1L8 2z" fill="var(--ink)"/></svg><span class="phone-number">+61 400 555 364</span></li>
      <li><svg viewBox="0 0 24 24"><path d="M2 10l10-7 10 7v10H2z" fill="var(--ink)"/><path d="M2 11l10 6 10-6" stroke="#fff" stroke-width="1.5" fill="none"/></svg>luke@wardoonacontracting.com.au</li>
      <li><svg viewBox="0 0 24 24" fill="none" stroke="var(--ink)" stroke-width="1.4"><circle cx="11" cy="11" r="9"/><ellipse cx="11" cy="11" rx="4" ry="9"/><path d="M2 11h18M4 6h14M4 16h14"/><path d="M15 15l6 6" stroke-width="2.5"/></svg>www.wardoonacontracting.com.au</li>
    </ul>
  </section>

</main>
</body>
</html>
```